AnswerCrafter Website Redesign

I'm looking to redesign our website AnswerCrafter.com. The main goal is to give it a fresh design that is easy on the eyes and pushes the users to creating an account.

Our platform is very simple and we only do one thing, we use ai to generate response to customer and product reviews.

See attached file to see the pricing section style.

On the homepage just under the hero section, I would like to include the wording:
"Write replies to the reviews you get on sites like:" then show the logos like we have on our register page: https://app.answercrafter.com/public/index.php

Target Market(s)

Business owners with brick and morter business or any business or product that gets online reviews

Industry/Entity Type

reputation management

Number of Pages Required

2 page

Requirements
Must have
• Home page and pricing page

```html
<!DOCTYPE html>
<html lang="en">
<head>
<meta charset="utf-8">
<title>AnswerCrafter – AI replies to your reviews</title>
<link href="https://fonts.googleapis.com/css2?family=Catamaran:wght@500;600;700;800&family=Arimo:wght@400;700&display=swap" rel="stylesheet">
<style>
:root{
  --navy:#213f99;
  --blue:#2b5ce6;
  --band:#1f44a3;
  --band-light:#3556b0;
  --yellow:#f5c518;
  --ink:#1b1b1b;
  --muted:#555a66;
  --line:#dcdfe8;
  --lavender:#eef0fb;
  --soft:#f5f6fc;
  --green:#8cc63f;
}
*{box-sizing:border-box;margin:0;padding:0}
html,body{width:1200px;height:4409px;overflow:hidden}
body{position:relative;background:#fff;font-family:"Arimo",Arial,sans-serif;color:var(--ink)}
.abs{position:absolute}
.head{font-family:"Catamaran",Arial,sans-serif}
.brand{display:flex;align-items:center;gap:10px;font-family:"Catamaran",Arial,sans-serif;font-weight:800;font-size:28px;color:var(--navy)}
.brand .mark{width:30px;height:30px;background:var(--navy);border-radius:4px}
.brand.light{color:#fff}.brand.light .mark{background:#fff}
.nav{top:34px;left:640px;display:flex;gap:26px;font-size:13px;color:#222}
.btn{display:flex;align-items:center;justify-content:center;border-radius:30px;font-size:12px;font-weight:700;color:#fff;background:var(--blue);letter-spacing:.3px}
.btn.yellow{background:var(--yellow);color:#1b1b1b}
.btn.grad{background:linear-gradient(90deg,#3a6cf0,#1f44a3);border-radius:24px}
.hero-title{left:60px;top:232px;font-size:52px;line-height:63px;font-weight:700;color:var(--navy)}
.hero-title em{font-style:normal;color:var(--yellow)}
.sites{display:flex;gap:16px;font-size:13px;font-weight:700;color:#444}
.sites.faded{color:#c7cad3}
.card{background:#fff;border-radius:10px;box-shadow:0 6px 24px rgba(30,50,120,.12)}
.reply{border:1px solid var(--line);border-radius:8px;padding:10px 12px;font-size:12px;line-height:21px;color:#666}
.photo{border-radius:10px}
.tabs{top:958px;left:60px;width:1080px;height:72px;border-bottom:1px solid var(--line)}
.tab{position:absolute;top:0;width:240px;text-align:center;font-family:"Catamaran",Arial,sans-serif;font-size:22px;line-height:26px;color:#222;font-weight:500}
.tab.active{color:var(--navy);font-weight:700}
.band{left:0;width:1200px;background:var(--band)}
.step .label{font-size:13px;color:var(--yellow)}
.step h3{font-family:"Catamaran",Arial,sans-serif;font-size:23px;color:#fff;font-weight:700;margin:4px 0 12px}
.step p{font-size:12.5px;line-height:22px;color:#e4e9fa}
.field{border:1px solid #c8ccd8;border-radius:6px;height:40px;padding:0 14px;display:flex;align-items:center;font-size:12px;color:#333}
.plan{width:412px;height:615px;border:2px solid #c9cfe6;border-radius:4px;background:#fff;overflow:hidden}
.plan .top{height:125px;background:var(--soft);text-align:center;padding-top:36px}
.plan h3{font-family:"Catamaran",Arial,sans-serif;font-size:24px;font-weight:700}
.plan .top p{font-size:13px;color:var(--navy);margin-top:6px}
.feat-title{font-size:14px;font-weight:700}
.feats{list-style:none;font-size:14px;color:#555}
.feats li{height:37.5px;display:flex;align-items:center;gap:14px}
.tick{width:14px;height:14px}
.faq{left:60px;width:525px;background:var(--soft);font-size:14px;color:#222;display:flex;align-items:center;justify-content:space-between;padding:0 18px}
.faq .plus{font-size:22px;color:var(--navy)}
</style>
</head>
<body>

<!-- header -->
<div class="abs brand" style="left:60px;top:26px"><span class="mark"></span>AnswerCrafter</div>
<nav class="abs nav"><span>Why Reply?</span><span>How It Works</span><span>Pricing</span><span>Blog</span><span>Login</span></nav>
<div class="abs btn" style="left:1027px;top:24px;width:113px;height:42px">TRY FREE</div>

<!-- hero -->
<div class="abs" style="left:860px;top:-120px;width:560px;height:870px;border-radius:50%;background:#f1f3fc"></div>
<h1 class="abs hero-title head">Write personalized<br>Responses to Reviews in<br>10 seconds! <em>(NO JOKE)</em></h1>
<div class="abs btn" style="left:60px;top:455px;width:164px;height:46px">START FOR FREE</div>
<div class="abs btn yellow" style="left:233px;top:455px;width:142px;height:46px">LEARN MORE</div>
<p class="abs" style="left:60px;top:562px;font-size:15px">Write replies to the reviews you get on sites like:</p>
<div class="abs sites" style="left:60px;top:604px"><span>Searchly</span><span>Staybnest</span><span>Marketon</span><span>TrustMeter</span><span>Yapper</span><span>TripVista</span><span>Handmarkt</span></div>

<div class="abs card" style="left:652px;top:220px;width:295px;height:320px;border-radius:0;border:2px solid #dfe4f5;box-shadow:none"></div>
<div class="abs" style="left:645px;top:197px;width:48px;height:48px;background:var(--navy);border-radius:6px">
  <svg width="48" height="48" viewBox="0 0 48 48"><circle cx="24" cy="25" r="11" fill="none" stroke="#fff" stroke-width="2.5"/><path d="M24 19v7l4 3" stroke="#fff" stroke-width="2.5" fill="none"/></svg>
</div>
<p class="abs head" style="left:674px;top:250px;font-size:18px;font-weight:700">Here Are Your Replies!</p>
<div class="abs reply" style="left:668px;top:295px;width:268px;background:#fff">Thank you so much for your kind words! we will so glad you enjoyed our services. we apperaciate your feedback</div>
<div class="abs reply" style="left:668px;top:392px;width:268px;background:#fff">Hello alex! we are delighted that your experience has been so positive. we are to see you very soon.</div>
<div class="abs reply" style="left:668px;top:485px;width:268px;background:#fff">5 stars review! Thank You .</div>

<div class="abs card" style="left:920px;top:160px;width:155px;height:118px;padding:12px">
  <p style="font-size:11px;color:var(--blue)">Replies Progress</p>
  <p style="font-size:16px;font-weight:700;margin-top:8px">62% <span style="font-size:8px;color:#888;font-weight:400">180 replies to goal</span></p>
  <div style="height:5px;background:#e7eaf4;border-radius:3px;margin-top:6px"><div style="width:62%;height:5px;background:var(--navy);border-radius:3px"></div></div>
  <p style="font-size:7px;color:#e59a1a;margin-top:10px">4.54 ★★★★★ <span style="color:#999">(365)</span></p>
</div>
<div class="abs photo" role="img" aria-label="Smiling woman holding a phone" style="left:890px;top:340px;width:240px;height:340px;background:linear-gradient(180deg,#7a4a32,#e4dfdb 50%,#cfd2d8);border-radius:120px 120px 10px 10px"></div>

<div class="abs card" style="left:585px;top:525px;width:190px;height:120px;padding:10px">
  <p style="font-size:11px;color:var(--blue)">Replies Progress <span style="font-size:7px;color:#666;margin-left:14px">Last Week</span></p>
  <p style="position:absolute;left:10px;top:78px;font-size:16px">86%</p>
  <svg style="position:absolute;left:68px;top:30px" width="112" height="84" viewBox="0 0 112 84">
    <g fill="#fbe7a0"><rect x="2" y="42" width="10" height="22"/><rect x="17" y="46" width="10" height="18"/><rect x="32" y="38" width="10" height="26"/><rect x="62" y="44" width="10" height="20"/><rect x="77" y="36" width="10" height="28"/><rect x="92" y="48" width="10" height="16"/></g>
    <rect x="47" y="22" width="10" height="42" fill="#f5c518"/><rect x="42" y="6" width="20" height="11" rx="2" fill="#111"/><text x="52" y="14.5" font-size="7" fill="#fff" text-anchor="middle" font-family="Arimo">72%</text>
    <g font-size="7" fill="#333" font-family="Arimo" text-anchor="middle"><text x="7" y="78">M</text><text x="22" y="78">T</text><text x="37" y="78">W</text><text x="52" y="78">T</text><text x="67" y="78">F</text><text x="82" y="78">S</text><text x="97" y="78">S</text></g>
  </svg>
</div>

<!-- intro -->
<h2 class="abs head" style="left:220px;top:782px;width:760px;text-align:center;font-size:29px;line-height:38px;font-weight:700">It's simple. Our tool Writes Replies and Responses to the Reviews your Customers leave. Doesn't Matter if it's 1 or 5 stars.</h2>
<div class="abs tabs">
  <div class="tab active" style="left:0;top:12px">Improved SEO</div>
  <div class="tab" style="left:283px">Build Customer<br>Trust</div>
  <div class="tab" style="left:557px">Increase Customer<br>Loyalty</div>
  <div class="tab" style="left:830px">Convert New<br>Customers</div>
  <div style="position:absolute;left:75px;bottom:-3px;width:78px;height:4px;background:var(--yellow)"></div>
</div>

<!-- seo -->
<div class="abs" style="left:92px;top:1090px;width:468px;height:600px;background:var(--lavender);border-radius:10px"></div>
<div class="abs" style="left:112px;top:1104px;display:flex;gap:8px"><span style="width:12px;height:12px;border-radius:50%;background:#fff"></span><span style="width:12px;height:12px;border-radius:50%;background:#fff"></span><span style="width:12px;height:12px;border-radius:50%;background:#fff"></span></div>
<div class="abs" style="left:112px;top:1130px;width:428px;height:535px;background:#fff;border-radius:6px"></div>
<div class="abs" style="left:133px;top:1145px;width:382px;height:217px;border:1px solid var(--line);border-radius:8px"></div>
<div class="abs" role="img" aria-label="Client portrait" style="left:152px;top:1164px;width:58px;height:58px;border-radius:50%;background:linear-gradient(180deg,#6b5548,#2e3542)"></div>
<p class="abs" style="left:228px;top:1164px;color:var(--yellow);font-size:15px">★★★★★</p>
<p class="abs" style="left:230px;top:1188px;font-size:12px;font-weight:700;color:var(--navy)">CLIENT NAME</p>
<p class="abs" style="left:440px;top:1157px;font-size:14px;font-weight:700;color:#6b85d8">Searchly</p>
<p class="abs" style="left:152px;top:1235px;width:350px;font-size:12px;line-height:22px;color:#666">Lorem Ipsum has been the industry's standard text ever since the thatis, when an unknown printer took a galley of type and scrambled it specimen book. Lorem Ipsum has been the industry's standard text ever since the thatis, when an unknown printer took.....</p>
<p class="abs" style="left:139px;top:1396px;font-size:16px;font-weight:700">Respone From The Owner <span style="font-size:10px;color:#888;font-weight:400;margin-left:6px">Just Now</span></p>
<div class="abs reply" style="left:133px;top:1437px;width:382px;height:80px">Thank you so much for your kind words! we will so glad you enjoyed our services. we apperaciate your feedback</div>
<div class="abs reply" style="left:133px;top:1533px;width:382px;height:79px;padding-top:16px">Hello alex! we are delighted that your experience has been so positive. we are to see you very soon.</div>
<div class="abs card" style="left:443px;top:1510px;width:187px;height:122px;padding:10px">
  <p style="font-size:11px;color:var(--blue)">Replies Progress <span style="font-size:7px;color:#666;margin-left:14px">Last Week</span></p>
  <p style="position:absolute;left:10px;top:82px;font-size:16px">86%</p>
  <svg style="position:absolute;left:68px;top:32px" width="112" height="84" viewBox="0 0 112 84">
    <g fill="#fbe7a0"><rect x="2" y="42" width="10" height="22"/><rect x="17" y="46" width="10" height="18"/><rect x="32" y="38" width="10" height="26"/><rect x="62" y="44" width="10" height="20"/><rect x="77" y="36" width="10" height="28"/><rect x="92" y="48" width="10" height="16"/></g>
    <rect x="47" y="22" width="10" height="42" fill="#f5c518"/><rect x="42" y="6" width="20" height="11" rx="2" fill="#111"/><text x="52" y="14.5" font-size="7" fill="#fff" text-anchor="middle" font-family="Arimo">72%</text>
    <g font-size="7" fill="#333" font-family="Arimo" text-anchor="middle"><text x="7" y="78">M</text><text x="22" y="78">T</text><text x="37" y="78">W</text><text x="52" y="78">T</text><text x="67" y="78">F</text><text x="82" y="78">S</text><text x="97" y="78">S</text></g>
  </svg>
</div>
<h2 class="abs head" style="left:650px;top:1290px;font-size:35px;font-weight:700;color:var(--navy)">Improved SEO</h2>
<p class="abs" style="left:651px;top:1349px;width:420px;font-size:14px;line-height:26px">Searchly loves seeing you leave a reply to your reviews and will give you a boost in their search results and local SEO.</p>
<div class="abs sites faded" style="left:652px;top:1426px"><span style="color:#5b78cf">Searchly</span><span>Staybnest</span><span>Marketon</span><span>TrustMeter</span><span>Yapper</span><span>TripVista</span><span>Handmarkt</span></div>

<!-- how it works -->
<div class="abs band" style="top:1765px;height:788px"></div>
<h2 class="abs head" style="left:0;top:1830px;width:1200px;text-align:center;font-size:36px;font-weight:700;color:#fff">How It Works</h2>
<div class="abs" style="left:60px;top:1945px;width:390px;height:188px;background:var(--band-light);border-radius:4px"></div>
<div class="abs step" style="left:112px;top:1972px;width:320px">
  <p class="label">STEP #1 Create an account</p><h3>1 minute account creation</h3>
  <p>Gain access to the most powerful tool for writing unique and personal responses to the reviews your customers leave your business.</p>
</div>
<svg class="abs" style="left:70px;top:1976px" width="28" height="28" viewBox="0 0 28 28" fill="none" stroke="#f5c518" stroke-width="2"><circle cx="12" cy="9" r="5"/><path d="M3 24c0-5 4-8 9-8s7 2 8 4M22 17v8M18 21h8"/></svg>
<div class="abs step" style="left:112px;top:2175px;width:320px">
  <p class="label">STEP #2 Copy and Paste The Review</p><h3>We make it way too simple!</h3>
  <p>Just copy the customer review and paste it into your account dashboard.</p>
</div>
<svg class="abs" style="left:65px;top:2178px" width="30" height="20" viewBox="0 0 30 20" fill="none" stroke="#f5c518" stroke-width="2"><rect x="1" y="2" width="28" height="16" rx="2"/><circle cx="9" cy="10" r="2"/><circle cx="15" cy="10" r="2"/><circle cx="21" cy="10" r="2"/></svg>
<div class="abs step" style="left:112px;top:2332px;width:320px">
  <p class="label">STEP #3 Personalized Response in Seconds</p><h3>Only a 10 second wait</h3>
  <p>In just seconds you'll receive 3 unique and personal responses. Choose the reply you like best or tell our system to generate 3 more.</p>
</div>
<svg class="abs" style="left:65px;top:2332px" width="28" height="28" viewBox="0 0 28 28" fill="none" stroke="#f5c518" stroke-width="2"><circle cx="14" cy="14" r="11"/><path d="M14 8v7l4 2"/></svg>

<div class="abs" style="left:578px;top:1990px;width:545px;height:397px;background:#3a5cb6;border-radius:14px"></div>
<div class="abs" style="left:600px;top:2012px;width:505px;height:353px;background:#fff;border-radius:6px"></div>
<div class="abs" role="img" aria-label="Blushing smiley emoji" style="left:660px;top:1973px;width:46px;height:46px;border-radius:50%;background:#f7c531"></div>
<div class="abs" style="left:1080px;top:2337px;width:60px;height:60px;border-radius:50%;background:var(--yellow)"></div>
<div class="abs brand" style="left:744px;top:2082px;font-size:34px"><span class="mark" style="width:36px;height:36px"></span>AnswerCrafter</div>
<div class="abs field" style="left:652px;top:2172px;width:392px">Enter Name *</div>
<div class="abs field" style="left:652px;top:2225px;width:392px">Enter Email *</div>
<div class="abs btn" style="left:770px;top:2280px;width:164px;height:44px">START FOR FREE</div>

<!-- pricing -->
<h2 class="abs head" style="left:0;top:2618px;width:1200px;text-align:center;font-size:34px;line-height:45px;font-weight:700">Never worry About Having to come Up with a Unique<br>Response to Each Review Ever Again!</h2>
<p class="abs" style="left:0;top:2727px;width:1200px;text-align:center;font-size:14px;color:var(--navy)">If your business, product or service receives reviews, this tool will save you hundreds of hours.</p>

<div class="abs plan" style="left:177px;top:2795px">
  <div class="top"><h3>Monthly Subscriptions</h3><p>Perfect for getting started for one business/product</p></div>
  <p style="text-align:center;font-size:18px;margin-top:30px">Starts at $9.99 / month</p>
  <div style="display:flex;justify-content:space-between;font-size:12px;margin:22px 25px 0">
    <span>50K</span><span>700K+</span></div>
  <div style="position:relative;height:8px;margin:10px 25px 0;background:#dfe3f0;border-radius:4px"><div style="width:25%;height:8px;background:var(--navy);border-radius:4px"></div><div style="position:absolute;left:22%;top:-9px;width:26px;height:26px;border-radius:50%;border:3px solid var(--navy);background:#fff"></div></div>
  <p style="text-align:center;font-size:13px;margin-top:20px">5000 word credits/ mo</p>
  <div class="btn grad" style="margin:20px 25px 0;height:44px">START FOR FREE</div>
  <p class="feat-title" style="margin:32px 25px 10px">AI Features individuals want:</p>
  <ul class="feats" style="margin:0 25px">
    <li><svg class="tick" viewBox="0 0 14 14"><path d="M1 7l4 4 8-9" fill="none" stroke="#8cc63f" stroke-width="2"/></svg>Personalized responses</li>
    <li><svg class="tick" viewBox="0 0 14 14"><path d="M1 7l4 4 8-9" fill="none" stroke="#8cc63f" stroke-width="2"/></svg>30+ Languages</li>
    <li><svg class="tick" viewBox="0 0 14 14"><path d="M1 7l4 4 8-9" fill="none" stroke="#8cc63f" stroke-width="2"/></svg>Auto-Save</li>
    <li><svg class="tick" viewBox="0 0 14 14"><path d="M1 7l4 4 8-9" fill="none" stroke="#8cc63f" stroke-width="2"/></svg>Revision History</li>
    <li><svg class="tick" viewBox="0 0 14 14"><path d="M1 7l4 4 8-9" fill="none" stroke="#8cc63f" stroke-width="2"/></svg>Assign members usage limits</li>
  </ul>
</div>

<div class="abs plan" style="left:612px;top:2795px">
  <div class="top"><h3>Agency Subscriptions</h3><p>Perfect for multiple clients/products per month</p></div>
  <p style="text-align:center;font-size:18px;margin-top:68px">Starting at $75.00 / month</p>
  <div class="btn grad" style="margin:74px 25px 0;height:44px">START FOR FREE</div>
  <p class="feat-title" style="margin:32px 25px 10px">AI Features individuals want:</p>
  <ul class="feats" style="margin:0 25px">
    <li><svg class="tick" viewBox="0 0 14 14"><path d="M1 7l4 4 8-9" fill="none" stroke="#8cc63f" stroke-width="2"/></svg>Everything in the Startup plan</li>
    <li><svg class="tick" viewBox="0 0 14 14"><path d="M1 7l4 4 8-9" fill="none" stroke="#8cc63f" stroke-width="2"/></svg>Dedicated Account Manager</li>
    <li><svg class="tick" viewBox="0 0 14 14"><path d="M1 7l4 4 8-9" fill="none" stroke="#8cc63f" stroke-width="2"/></svg>Onboarding &amp; Training</li>
    <li><svg class="tick" viewBox="0 0 14 14"><path d="M1 7l4 4 8-9" fill="none" stroke="#8cc63f" stroke-width="2"/></svg>Unlimited Integrations</li>
  </ul>
</div>

<!-- faq -->
<h2 class="abs head" style="left:0;top:3490px;width:1200px;text-align:center;font-size:36px;font-weight:700">Frequently Asked Questions</h2>
<div class="abs faq" style="top:3597px;height:44px;background:var(--navy);color:#fff">Why is it important to respond to Searchly reviews?<span style="font-size:20px">−</span></div>
<p class="abs" style="left:82px;top:3658px;width:470px;font-size:11.5px;line-height:22px;color:#444">Responding to Searchly reviews is vital for your business's success in local search results. By responding to both negative and positive feedback, you show customers that you're committed to listening to their concerns and exceeding their expectations.</p>
<div class="abs faq" style="top:3763px;height:44px">Why is it important to respond to negative reviews?<span class="plus">+</span></div>
<div class="abs faq" style="top:3827px;height:62px"><span style="width:440px;line-height:20px">How can I trust someone who doesn't work at my business to reply to reviews on my behalf?</span><span class="plus">+</span></div>
<div class="abs faq" style="top:3898px;height:44px">Which online review sites does AnswerCrafter.com support?<span class="plus">+</span></div>

<div class="abs card" style="left:883px;top:3555px;width:257px;height:295px;border-radius:18px;border:2px solid #dfe4f5;box-shadow:none"></div>
<p class="abs head" style="left:900px;top:3585px;font-size:17px;font-weight:700">Here Are Your Replies!</p>
<div class="abs" style="left:1108px;top:3562px;width:38px;height:38px;background:var(--yellow);border-radius:6px"><svg width="38" height="38" viewBox="0 0 38 38"><circle cx="19" cy="20" r="9" fill="none" stroke="#fff" stroke-width="2"/><path d="M19 15v6l3 2" stroke="#fff" stroke-width="2" fill="none"/></svg></div>
<div class="abs reply" style="left:900px;top:3625px;width:225px;font-size:10px;line-height:17px;background:#fff">Thank you so much for your kind words! we will so glad you enjoyed our services. we apperaciate your feedback</div>
<div class="abs reply" style="left:900px;top:3708px;width:225px;font-size:10px;line-height:17px;background:#fff">Hello alex! we are delighted that your experience has been so positive. we are to see you very soon.</div>
<div class="abs reply" style="left:900px;top:3786px;width:225px;font-size:10px;background:#fff">5 stars review! Thank You .</div>
<div class="abs photo" role="img" aria-label="Smiling woman in a grey cardigan" style="left:720px;top:3580px;width:240px;height:425px;background:linear-gradient(180deg,#4a3328,#e5d3c6 35%,#b9bbbe);border-radius:120px 120px 0 0"></div>

<!-- cta -->
<div class="abs band" style="top:4005px;height:404px"></div>
<h2 class="abs head" style="left:62px;top:4075px;font-size:54px;line-height:60px;font-weight:800;color:#fff">Ready to give Reply to<br>Reviews a <span style="color:var(--yellow)">Try?</span></h2>
<p class="abs" style="left:62px;top:4210px;font-size:15px;color:#fff">Get started today with one FREE Reply to your Review. No credit card required.</p>
<div class="abs btn yellow" style="left:860px;top:4128px;width:148px;height:42px">TRY FOR FREE</div>
<svg class="abs" style="left:760px;top:4110px" width="340" height="130" viewBox="0 0 340 130" fill="none" stroke="#fff" stroke-width="1.6">
  <path d="M10 20l8 14 3-6 6 5 3-3-6-5 6-2z"/><path d="M290 15l8 14 3-6 6 5 3-3-6-5 6-2z"/><path d="M290 73l8 14 3-6 6 5 3-3-6-5 6-2z"/><path d="M30 95l8 14 3-6 6 5 3-3-6-5 6-2z"/><path d="M110 95l8 14 3-6 6 5 3-3-6-5 6-2z"/><path d="M222 102l8 14 3-6 6 5 3-3-6-5 6-2z"/><path d="M175 60l8 14 3-6 6 5 3-3-6-5 6-2z"/>
</svg>

<!-- footer -->
<div class="abs brand light" style="left:60px;top:4348px;font-size:24px"><span class="mark" style="width:26px;height:26px"></span>AnswerCrafter</div>
<p class="abs" style="left:860px;top:4345px;width:278px;text-align:right;font-size:11px;color:#fff">©2023 <span style="color:var(--yellow)">answercrafter</span> - All rights reserved.</p>
<p class="abs" style="left:760px;top:4373px;width:378px;text-align:right;font-size:11px;color:#fff">Blog &nbsp; | &nbsp; Privacy Policy &nbsp; | &nbsp; Contact &nbsp; | &nbsp; Sitemap</p>

</body>
</html>
```